Email Banner for Technology Company

We need a new email banner. The purpose of the email banner is to make us look more professional as a business and keep all communications with clients uniform. The previous designs which we have included below have now become outdated as our brand has developed and we need the new banner to become more aligned and modern.

We are a marketing organization that specialises in lead generation, email newsletters are sent to prospects on a regular basis. Therefore, it is important that we have an aesthetically pleasing banner as this is the first real impression prospects have our business. First impressions matter.

We are looking for a new email banner design as the current design is now outdated and does not reflect who we are as a business.

The new banners are required for launch at the start of Q2.

There is future work in the pipeline for the winning design. We have multiple industry sites that will require the new design as well as creating each of these in multiple languages.

The design must include the Zevomarkly wording the tagline 'The Ultimate Research Library for Technology Pro's.
It needs to be creative and fun but still remain professional, sticking with the colour theme that already exists.

Requirements
Must have
• The design must include the Zevomarkly wording the tagline 'The Ultimate Research Library for Technology Pro's.

```html
<!DOCTYPE html>
<html lang="en">
<head>
<meta charset="utf-8">
<title>Zevomarkly Email Banner</title>
<link rel="stylesheet" href="https://fonts.googleapis.com/css2?family=Sora:wght@300;400;500;700&display=swap">
<style>
  :root {
    --page-bg: #ffffff;
    --brand-blue: #03aeef;
    --sky-blue: #73cdf4;
    --white: #ffffff;
    --ink: #000000;
    --deco-tone: rgba(255, 255, 255, 0.35);
  }
  html, body {
    margin: 0;
    padding: 0;
    width: 1200px;
    height: 896px;
    overflow: hidden;
    background: var(--page-bg);
  }
  .canvas {
    position: relative;
    width: 1200px;
    height: 896px;
  }
  .email-banner {
    position: absolute;
    left: 102px;
    top: 412px;
    width: 1023px;
    height: 164px;
    overflow: hidden;
    font-family: "Sora", sans-serif;
    background: var(--brand-blue);
  }
  .banner-shapes {
    position: absolute;
    inset: 0;
  }
  .deco-area {
    position: absolute;
    background: linear-gradient(160deg, rgba(255,255,255,0.45), rgba(255,255,255,0.2));
  }
  .deco-rings-top {
    left: 54px;
    top: 0;
    width: 166px;
    height: 83px;
    border-radius: 0 0 83px 83px;
  }
  .deco-rings-bottom {
    left: 30px;
    top: 111px;
    width: 106px;
    height: 53px;
    border-radius: 53px 53px 0 0;
  }
  .deco-dots {
    left: 405px;
    top: 14px;
    width: 150px;
    height: 128px;
    border-radius: 16px;
  }
  .wordmark {
    position: absolute;
    left: 64px;
    top: 66px;
    margin: 0;
    font-size: 44px;
    font-weight: 700;
    letter-spacing: -2.2px;
    line-height: 1;
    color: var(--ink);
  }
  .tagline {
    position: absolute;
    left: 677px;
    top: 58px;
    margin: 0;
    font-size: 21.5px;
    font-weight: 300;
    line-height: 24px;
    letter-spacing: -0.4px;
    color: var(--white);
  }
  .tagline-highlight {
    font-weight: 500;
    display: inline-block;
    border-bottom: 3px solid var(--white);
    line-height: 22px;
  }
  .cta-tab {
    position: absolute;
    right: 0;
    bottom: 0;
    width: 108px;
    height: 30px;
    background: var(--white);
    border-top-left-radius: 30px;
    display: flex;
    align-items: center;
    justify-content: center;
    padding-left: 10px;
    box-sizing: border-box;
    font-size: 12px;
    font-weight: 400;
    letter-spacing: -0.3px;
    color: var(--ink);
    text-decoration: none;
  }
</style>
</head>
<body>
<div class="canvas">
  <section class="email-banner">
    <svg class="banner-shapes" width="1023" height="164" viewBox="0 0 1023 164" aria-hidden="true">
      <polygon class="diagonal-panel" points="460,0 1023,0 1023,164 612,164" fill="var(--sky-blue)"/>
    </svg>

    <div class="deco-area deco-rings-top" role="img" aria-label="Decorative concentric white rings"></div>
    <div class="deco-area deco-rings-bottom" role="img" aria-label="Decorative concentric white rings"></div>
    <div class="deco-area deco-dots" role="img" aria-label="Decorative scatter of white dots"></div>

    <h1 class="wordmark">Zevomarkly</h1>

    <p class="tagline">The Ultimate Research<br>Library for <span class="tagline-highlight">Technology Pro's</span></p>

    <a class="cta-tab" href="#">Click Here</a>
  </section>
</div>
</body>
</html>
```